Trading company need to develop packaging design for a new nuts brand.

We need a packaging design for a new nuts brand.
- Packaging format - doypack packaging with zip lock 150 g - 150x220mm
- Product line will include all possible types of nuts. We would like to take a pistachio like an exampl for developing design.
- The main task is to connect the whole concept to the chameleon character /hero (Example of the image is in Uploaded files, but you don't need to use it)
- In design we expect modern, creative and non-standard solutions, we focus on minimalism
- Packaging mustn’t be transparent or craft
- The future product will be a premium segment
- We expect front and back design of packaging
- Our competitors: Tovren and Halvinder (Examples of competitors' packaging, I will attach in Uploaded files)
- Future brand would be sold in different countries therefore the design must be universal, not connect to any region, country or place of nuts growth.

```html
<!DOCTYPE html>
<html lang="en">
<head>
<meta charset="utf-8">
<title>Pistachio Pouch – Front</title>
<link rel="stylesheet" href="https://fonts.googleapis.com/css2?family=Kaushan+Script&family=Oswald:wght@500;600;700&family=Montserrat:wght@500;700&family=Arvo:wght@700&display=swap">
<style>
  :root {
    --page: #ffffff;
    --kraft-light: #efe3c9;
    --kraft: #e4d4b1;
    --leaf: #5e7a1f;
    --leaf-dark: #3f5712;
    --cocoa: #4a2a10;
    --cocoa-soft: #c9a27a;
    --cream: #f3ecdc;
    --nut: #e8dcae;
    --bowl: #8a4a2a;
  }
  * { margin: 0; padding: 0; box-sizing: border-box; }
  html, body { width: 1200px; height: 1200px; overflow: hidden; background: var(--page); }
  .canvas { position: relative; width: 1200px; height: 1200px; }

  .pouch {
    position: absolute; left: 283px; top: 96px; width: 640px; height: 1010px;
    background: radial-gradient(ellipse at 60% 40%, var(--kraft-light) 0%, var(--kraft) 80%);
    clip-path: polygon(14px 0, 626px 0, 640px 22px, 640px 1010px, 0 1010px, 0 22px);
    overflow: hidden;
  }
  .nut-column {
    position: absolute; left: 0; top: 0; width: 177px; height: 885px;
    background: linear-gradient(180deg, #e2d59f 0%, #d9cc96 45%, #e6dcae 100%);
    border-bottom-right-radius: 60px;
  }
  .brand-band {
    position: absolute; left: 178px; top: 0; width: 215px; height: 376px;
    background: linear-gradient(180deg, var(--leaf) 0%, #587318 100%);
    display: flex; flex-direction: column; align-items: center; justify-content: flex-end;
    padding-bottom: 90px; gap: 14px;
  }
  .brand-mark { width: 22px; height: 22px; border-radius: 50%; background: var(--cream); }
  .brand-name {
    font-family: "Montserrat", sans-serif; font-weight: 700; font-size: 30px;
    letter-spacing: 2px; color: var(--cream);
  }
  .title {
    position: absolute; left: 82px; top: 398px;
    font-family: "Kaushan Script", cursive; font-weight: 400; font-size: 122px; line-height: 1;
    color: var(--cocoa); text-shadow: 3px 3px 0 var(--cocoa-soft);
    white-space: nowrap;
  }
  .variant {
    position: absolute; left: 141px; top: 588px; width: 380px; height: 44px;
    background: var(--leaf); border-radius: 22px 0 0 22px;
    font-family: "Oswald", sans-serif; font-weight: 600; font-size: 28px; line-height: 1;
    color: var(--cream); letter-spacing: 2px; white-space: nowrap;
    display: flex; align-items: center; padding-left: 32px;
  }
  .organic {
    position: absolute; left: 186px; top: 752px; width: 108px; color: var(--cocoa);
    font-family: "Oswald", sans-serif; text-align: center; line-height: 1;
  }
  .organic .pct { display: block; font-size: 44px; font-weight: 700; font-style: italic; }
  .organic .word { display: block; font-size: 34px; font-weight: 600; margin-top: 6px; }
  .bottom-band {
    position: absolute; left: 0; bottom: 0; width: 100%; height: 124px;
    background: linear-gradient(180deg, var(--leaf) 0%, var(--leaf-dark) 100%);
  }
  .claims {
    position: absolute; left: 79px; top: 14px;
    font-family: "Montserrat", sans-serif; font-weight: 500; font-size: 10px;
    color: var(--cream); line-height: 20px; letter-spacing: 0.3px; white-space: nowrap;
  }
  .net-weight {
    position: absolute; left: 309px; top: 66px; white-space: nowrap;
    font-family: "Arvo", serif; font-weight: 700; color: #ffffff; font-size: 19px;
  }
  .net-weight b { font-size: 27px; }
  .bowl {
    position: absolute; left: 433px; top: 538px; width: 420px; height: 420px;
    border-radius: 50%;
    background: radial-gradient(circle at 50% 50%, #eee2bf 0%, var(--nut) 62%, #a35e36 64%, var(--bowl) 72%);
  }
</style>
</head>
<body>
<div class="canvas">
  <div class="pouch">
    <div class="nut-column" role="img" aria-label="Photo of roasted pistachios in their shells scattered down the left edge"></div>
    <div class="brand-band">
      <span class="brand-mark"></span>
      <span class="brand-name">VERDALO</span>
    </div>
    <h1 class="title">Pistachio</h1>
    <div class="variant">Roasted and Salted</div>
    <div class="organic"><span class="pct">100%</span><span class="word">ORGANIC</span></div>
    <div class="bottom-band">
      <p class="claims">LOADED IN ANTIOXIDANTS | CHOLESTEROL FREE | GLUTEN FREE<br>GREAT FOR HEART HEALTH | GREAT FOR SKIN</p>
      <p class="net-weight">Net.Wt: <b>150g</b></p>
    </div>
    <div class="bowl" role="img" aria-label="Photo of a brown bowl filled with roasted pistachios"></div>
  </div>
</div>
</body>
</html>
```